Restaurant Email Club Sign Up Poster

Looking for a creative design that will catch people's eye and prompt them to sign up for our email club for our Restaurant that we run in Omaha, Nebraska. Open to any creative ways to most effectively grab peoples attention quickly without being too confusing. Want it to be simple but actionable.

Have attached some documents for your assistance - in addition to some marketing materials we have put out in the past.

Would like to put design on posters to hang up throughout the restaurant and likely will make stickers to put on check presenters as well.

Catchy stock photo or use of the cheese curd photo probably good idea - callout things mentioned in the "must haves" section below. Looking for most creative and catchy, yet simple design.

Target Market(s)

30-50 year olds males and females.

Industry/Entity Type

Restaurant

Requirements
Must have
• Must include callouts for -
• Sign up for E-Club for access to future offers and events (or something along these lines)
• Free Appetizer for Signing Up
• Free Birthday Meal
Should not have
• Please do not make this poster like the postcard that I attached to the project - this is not a poster to call out that we are a new burger and beer spot, that we have 40 rotating taps, or that we have 15 specialty burgers, etc. This is simply a poster to grab someones attention and get them to sign up for our email club. Should maybe have a catchy question, something like, "Want a Free Appetizer?" or something catchy and similar, and then below say "And access to future deals and event happenings?"

```html
<!DOCTYPE html>
<html lang="en">
<head>
<meta charset="utf-8">
<title>Prairie Tap House E-Club Poster</title>
<link href="https://fonts.googleapis.com/css2?family=Alfa+Slab+One&family=Mulish:wght@400;600;800&display=swap" rel="stylesheet">
<style>
  :root {
    --stage: #d6d6d6;
    --paper: #ffffff;
    --ink: #1a1a1a;
    --line: #111111;
    --band: rgba(200, 200, 200, 0.85);
    --food-warm: #e07a22;
    --food-deep: #b8561a;
    --food-light: #f2a245;
    --wood-light: #eceae6;
    --wood-mid: #c9c6c0;
  }
  * { margin: 0; padding: 0; box-sizing: border-box; }
  html, body { width: 1200px; height: 798px; overflow: hidden; }
  body {
    background: var(--stage);
    font-family: "Mulish", sans-serif;
    color: var(--ink);
    position: relative;
  }
  .poster {
    position: absolute;
    left: 313px; top: 18px;
    width: 574px; height: 762px;
    background: var(--paper);
    overflow: hidden;
  }
  .frame { position: absolute; inset: 0; pointer-events: none; }
  .brand {
    position: absolute;
    left: 210px; top: 18px; width: 154px;
    display: flex; align-items: center; justify-content: center; gap: 6px;
    font-weight: 800; font-size: 12.5px; letter-spacing: 0.5px;
    color: var(--ink);
  }
  .brand-square { width: 10px; height: 10px; background: var(--ink); flex: none; }
  .lead {
    position: absolute; left: 0; right: 0; top: 107px;
    text-align: center;
    font-weight: 400; font-size: 26px; letter-spacing: 0.3px;
  }
  .headline { position: absolute; left: 0; top: 140px; width: 574px; height: 250px; }
  .headline text { font-family: "Alfa Slab One", serif; fill: var(--ink); }
  .subline {
    position: absolute; left: 0; right: 0; top: 380px;
    text-align: center;
    font-weight: 400; font-size: 12.6px; letter-spacing: 0.1px;
  }
  .table-photo {
    position: absolute; left: 0; top: 604px; width: 574px; height: 158px;
    background: linear-gradient(180deg, var(--wood-mid) 0%, var(--wood-light) 45%, var(--wood-mid) 100%);
  }
  .food-photo {
    position: absolute; left: 76px; top: 432px; width: 460px; height: 290px;
    background: radial-gradient(ellipse at 50% 45%, var(--food-light) 0%, var(--food-warm) 45%, var(--food-deep) 70%, rgba(255,255,255,0) 72%);
  }
  .serving-note {
    position: absolute; left: 440px; top: 696px; width: 118px;
    text-align: center;
    font-style: italic; font-size: 5.6px; line-height: 1.3;
    color: var(--ink);
  }
  .signup-band {
    position: absolute; left: 0; bottom: 6px; width: 574px; height: 28px;
    background: var(--band);
    display: flex; align-items: center; justify-content: center;
  }
  .signup-text {
    font-weight: 800; font-size: 19px; color: var(--ink);
    letter-spacing: 0.1px;
  }
</style>
</head>
<body>
  <main class="poster">
    <svg class="frame" width="574" height="762" viewBox="0 0 574 762" aria-hidden="true">
      <g stroke="var(--line)" stroke-width="2.4" fill="none">
        <polyline points="214,27 24,27 24,662 44,662"/>
        <polyline points="360,27 550,27 550,676 528,676"/>
      </g>
    </svg>

    <div class="brand"><span class="brand-square"></span>PRAIRIE TAP HOUSE</div>

    <p class="lead">JOIN OUR E-CLUB TO RECEIVE A</p>

    <svg class="headline" viewBox="0 0 574 250" aria-label="Free appetizer and birthday meal">
      <text x="70" y="120" font-size="148" textLength="438" lengthAdjust="spacingAndGlyphs">FREE</text>
      <text x="68" y="186" font-size="63" textLength="426" lengthAdjust="spacingAndGlyphs">APPETIZER</text>
      <text x="60" y="229" font-size="43" textLength="443" lengthAdjust="spacingAndGlyphs">&amp; BIRTHDAY MEAL</text>
    </svg>

    <p class="subline">AND GET ACCESS TO OUR LATEST DEALS AND EVENT HAPPENINGS</p>

    <div class="table-photo" role="img" aria-label="Photo of weathered white wooden tabletop"></div>
    <div class="food-photo" role="img" aria-label="Photo of a plate piled with golden fried cheese curds, one broken open with melted cheese, against soft white light rays"></div>

    <p class="serving-note">*ACTUAL CHEESE CURD<br>APPETIZER ORDER COMES WITH<br>9 LARGE CHEESE CURDS*</p>

    <div class="signup-band">
      <span class="signup-text">SIGN UP AT WWW.PRAIRIETAPHOUSE.COM</span>
    </div>
  </main>
</body>
</html>
```